Flyer Tally Your Ledger Free

Hi
Can you please design me a DL Flyer for: Tally Your Ledger Free
Info:
Starting a new Business ?
Want to save on bookkeeping fees for your existing business?

You can now save 1000's off bookkeeping fees by Doing it Yourself.

Using our Bookkeeper software you simply key in the information as you go.

We offer one on one training, backup and support.
We can assist you with BAS Preparation and Payrol Advice.

Add Modules as required:
Point of Sale Module
Jobs Management Module
Website Intergration Module

Fee set up assistance and training.

Lets get the ball rolling: 1300 642 815
www.tylfr.com.au
admin@tylfr.com.au (use the logo thing you made)

Target Market(s)

Small Business

Colors
ec1f27
f04a50
f59296
fcdcdc
ffffff

Requirements
Nice to have
• image/s related to bookkeeping

```html
<!DOCTYPE html>
<html lang="en">
<head>
<meta charset="utf-8">
<title>Tally Your Ledger Free – DL Flyer</title>
<link href="https://fonts.googleapis.com/css2?family=Oswald:wght@500;600&family=Roboto:ital,wght@0,400;0,500;0,700;1,700&display=swap" rel="stylesheet">
<style>
  :root{
    --red:#ec1f27;
    --red-mid:#f04a50;
    --pink:#f59296;
    --blush:#fcdcdc;
    --white:#ffffff;
    --ink:#1a1a1a;
    --grey:#6d6d6d;
    --stage:#707070;
    --brown:#6b3a24;
  }
  *{margin:0;padding:0;box-sizing:border-box}
  html,body{width:1200px;height:1200px;overflow:hidden}
  body{background:var(--stage);font-family:'Roboto',sans-serif;color:var(--ink);position:relative}
  .flyer{position:absolute;left:329px;top:51px;width:542px;height:1084px;background:var(--white);overflow:hidden;box-shadow:0 6px 24px rgba(0,0,0,.35)}
  .hero{position:absolute;left:0;top:0;width:542px;height:420px}
  .hero-title{position:absolute;left:0;top:0;width:542px;height:420px}
  .abs{position:absolute;left:0;width:100%;text-align:center}
  .lead-red{top:420px;color:var(--red);font-style:italic;font-weight:700;font-size:22px}
  .lead-q{top:450px;font-style:italic;font-weight:700;font-size:22px;line-height:29px}
  .save{top:527px;font-size:19px}
  .diy{top:552px;color:var(--red);font-weight:700;font-size:19px;letter-spacing:.2px}
  .benefits{position:absolute;left:22px;top:585px;width:494px;height:155px;border:1.5px solid var(--pink);padding:20px 24px 0 20px;list-style:none}
  .benefits li{position:relative;padding-left:31px;font-size:17.5px;line-height:23px}
  .benefits svg{position:absolute;left:0;top:1px;width:24px;height:22px}
  .benefits strong{font-weight:700}
  .modules-label{top:755px;font-size:16px;font-weight:500}
  .modules{position:absolute;left:24px;top:786px;width:500px;display:flex;justify-content:space-between}
  .module{display:flex;align-items:center;gap:7px;color:var(--red);font-size:15px;line-height:16px;text-transform:uppercase}
  .module-icon{width:54px;height:56px;border:2px solid var(--red);border-radius:3px;display:flex;align-items:center;justify-content:center}
  .module-icon span{width:42px;height:44px;background:var(--red);display:flex;align-items:center;justify-content:center}
  .fee{top:862px;font-size:17.5px}
  .cta-band{position:absolute;left:0;top:891px;width:100%;height:39px;background:var(--pink);color:var(--white);font-weight:700;font-size:22px;letter-spacing:.5px;text-align:center;line-height:39px}
  .contact-band{position:absolute;left:0;top:932px;width:100%;height:66px;background:var(--red);color:var(--white)}
  .contact-list{position:absolute;left:16px;top:10px;list-style:none;font-size:16px;line-height:22px}
  .contact-list li{display:flex;align-items:center;gap:9px}
  .contact-list svg{width:17px;height:17px}
  .web-pill{position:absolute;left:251px;top:14px;width:291px;height:36px;background:var(--white);border-radius:18px 0 0 18px;display:flex;align-items:center;padding-left:20px;gap:8px;color:var(--grey);font-weight:700;font-size:22px}
  .web-pill b{color:var(--red)}
  .brand{position:absolute;left:0;top:1020px;width:100%;display:flex;justify-content:center;align-items:center;gap:10px;color:var(--red);font-weight:500;font-size:27px}
  .brand-dot{width:26px;height:26px;border-radius:50%;border:2.5px solid var(--red)}
</style>
</head>
<body>
<main class="flyer">
  <svg class="hero" viewBox="0 0 542 420" role="img" aria-label="Photo of a person writing in a notebook beside a laptop on a wooden desk">
    <defs>
      <linearGradient id="heroTone" x1="0" y1="0" x2="0.6" y2="1">
        <stop offset="0" stop-color="#ec1f27"/>
        <stop offset="0.45" stop-color="#d9453e"/>
        <stop offset="0.7" stop-color="#8a4a2e"/>
        <stop offset="1" stop-color="#5e321f"/>
      </linearGradient>
    </defs>
    <polygon points="0,0 542,0 542,160 0,375" fill="url(#heroTone)"/>
  </svg>
  <svg class="hero-title" viewBox="0 0 542 420" aria-hidden="true">
    <g transform="translate(15 347) rotate(-28)">
      <text x="0" y="0" fill="#ffffff" font-family="Oswald, sans-serif" font-weight="500" font-size="56" textLength="279" lengthAdjust="spacingAndGlyphs">TALLY YOUR</text>
    </g>
    <g transform="translate(181 394) rotate(-28)">
      <rect x="-6" y="-96" width="480" height="96" fill="#f04a50"/>
      <text x="12" y="-12" fill="#ffffff" font-family="Oswald, sans-serif" font-weight="600" font-size="88" textLength="380" lengthAdjust="spacingAndGlyphs">LEDGER FREE</text>
    </g>
  </svg>

  <p class="abs lead-red">Starting a new Business ?</p>
  <p class="abs lead-q">Want to save on bookkeeping fees for your<br>existing business?</p>
  <p class="abs save">You can now save 1000's off bookkeeping fees by</p>
  <p class="abs diy">DOING IT YOURSELF:</p>

  <ul class="benefits">
    <li><svg viewBox="0 0 24 22"><circle cx="10" cy="12" r="9" fill="none" stroke="#ec1f27" stroke-width="2"/><path d="M5 11l5 5 12-14" fill="none" stroke="#ec1f27" stroke-width="2.4"/></svg>Using our Bookkeeper software you simply key in the information as you go.</li>
    <li><svg viewBox="0 0 24 22"><circle cx="10" cy="12" r="9" fill="none" stroke="#ec1f27" stroke-width="2"/><path d="M5 11l5 5 12-14" fill="none" stroke="#ec1f27" stroke-width="2.4"/></svg>We offer one on one training, backup and support.</li>
    <li><svg viewBox="0 0 24 22"><circle cx="10" cy="12" r="9" fill="none" stroke="#ec1f27" stroke-width="2"/><path d="M5 11l5 5 12-14" fill="none" stroke="#ec1f27" stroke-width="2.4"/></svg>We can assist you with:<br><strong>BAS Preparation and Payrol Advice.</strong></li>
  </ul>

  <p class="abs modules-label">Add Modules as required:</p>
  <div class="modules">
    <div class="module">
      <div class="module-icon"><span><svg width="30" height="30" viewBox="0 0 30 30"><circle cx="15" cy="15" r="11" fill="none" stroke="#fff" stroke-width="2" stroke-dasharray="14 4"/><text x="15" y="21" text-anchor="middle" fill="#fff" font-family="Roboto, sans-serif" font-weight="700" font-size="16">$</text></svg></span></div>
      <div>Point<br>of Sale<br>Module</div>
    </div>
    <div class="module">
      <div class="module-icon"><span><svg width="26" height="30" viewBox="0 0 26 30"><rect x="3" y="4" width="20" height="24" rx="2" fill="none" stroke="#fff" stroke-width="2"/><rect x="9" y="1" width="8" height="5" fill="#fff"/><path d="M7 12h12M7 17h12M7 22h12" stroke="#fff" stroke-width="2"/></svg></span></div>
      <div>Jobs<br>Management<br>Module</div>
    </div>
    <div class="module">
      <div class="module-icon"><span><svg width="30" height="30" viewBox="0 0 30 30"><circle cx="15" cy="15" r="12" fill="none" stroke="#fff" stroke-width="2"/><ellipse cx="15" cy="15" rx="5" ry="12" fill="none" stroke="#fff" stroke-width="2"/><path d="M3 15h24M5 9h20M5 21h20" stroke="#fff" stroke-width="1.6"/></svg></span></div>
      <div>Website<br>Integration<br>Module</div>
    </div>
  </div>

  <p class="abs fee">Fee set up assistance &amp; training.</p>

  <div class="cta-band">LETS GET THE BALL ROLLING</div>
  <div class="contact-band">
    <ul class="contact-list">
      <li><svg viewBox="0 0 20 20"><path d="M4 2l4 4-2 3c1 2 3 4 5 5l3-2 4 4-3 3C9 18 2 11 1 5z" fill="none" stroke="#fff" stroke-width="1.6"/></svg>1300 642 815</li>
      <li><svg viewBox="0 0 20 20"><rect x="1.5" y="4" width="17" height="12" fill="none" stroke="#fff" stroke-width="1.6"/><path d="M1.5 4l8.5 7 8.5-7" fill="none" stroke="#fff" stroke-width="1.6"/></svg>admin@tylfr.com.au</li>
    </ul>
    <div class="web-pill">
      <svg width="18" height="18" viewBox="0 0 20 20"><circle cx="10" cy="10" r="8" fill="none" stroke="#ec1f27" stroke-width="2"/><ellipse cx="10" cy="10" rx="3.5" ry="8" fill="none" stroke="#ec1f27" stroke-width="1.6"/><path d="M2 10h16" stroke="#ec1f27" stroke-width="1.6"/></svg>
      <span>www.ty<b>lfr</b>.com.au</span>
    </div>
  </div>

  <div class="brand"><span class="brand-dot"></span><span>Tally Your Ledger Free</span></div>
</main>
</body>
</html>
```